"Harlow's True Grain Woodwork" with a logo of a saw blade and handplane combined

Need a business card logo with a saw blade and hand plane
combined with Harlow's True Grain Woodwork on it, and a unique design.

Woodworking has been in my family for generations, from carpentry, to milling logs for old farm homes and barns in the 1930's and 1940's. My grandfather had a small carpentry business from his home,and passed his skills down to my father who also did woodworking from his own small business. Having the passion for woodwork in my blood, I'm trying to continue with my own small business doing custom fine woodwork such as tables, small cabinetry and even outdoor projects to suite the customers needs. All my projects start with a rough piece of lumber, what ever the species suited for the project, and is milled to dimensions , assembled, and finished all by hand for a true handcrafted project.

My target market would be people who want a custom handmade piece, something that they can't find in stores and is unique. Also people who are willing to pay and appreciate the value, which is sometimes a hard market to find.

As far as design, I think I would like to get a sleek looking saw blade on the card combined with a hand plane some how. Background colour maybe a dark wood texture or grey? Colours I like are grey, black, reds, white, yellows but depending on how the card is looking I'm not afraid to use a cool colour to make something stand out. Just want the card to flow ,look clean and unique. Lettering I like serif and script or something similar to these that looks good on the card.

Facebook page is under Harlow's True Grain Woodwork
Updates

If I could get logo on the card, a saw blade, hand plane or combine both together would be nice! Added Saturday, June 11, 2016

Target Market(s)

People that like a unique hand made project built to last

Industry/Entity Type

Business

Contact Information for Business Card

Harlows True Grain Woodwork
Hand crafted by: Owen Harlow
Phone: 905 718-2265
Address: 412 Birchmont Rd. Niagara-On-The-Lake Ont.
Email: harlowstruegrain@mailpost.example
Facebook: Harlows True Grain Woodwork
prefer icons for the info!

Font styles to use
Serif
Script

Requirements
Must have
• Nice clean look, little bit bold with an elegant taste
• Prefer black lettering
Nice to have
• I like silver for the saw blade and silver with brown handles on the hand plane!
Should not have
• Bright colours

```html
<!DOCTYPE html>
<html lang="en">
<head>
<meta charset="utf-8">
<title>Harlow's True Grain Woodwork — Business Card</title>
<link rel="stylesheet" href="https://fonts.googleapis.com/css2?family=Oswald:wght@600&family=Open+Sans:wght@400;700&display=swap">
<style>
  :root {
    --backdrop: #3a3532;
    --card-black: #0d0d0d;
    --card-brown: #6d420f;
    --brand-brown: #8a5416;
    --brand-brown-deep: #5a360b;
    --text-white: #f4f4f4;
    --text-soft: #d9d9d9;
    --silver: #c9c9c9;
    --silver-dark: #7a7a7a;
    --divider: #6a6a6a;
  }
  * { box-sizing: border-box; margin: 0; padding: 0; }
  html, body {
    width: 1200px; height: 900px; overflow: hidden;
    background: var(--backdrop);
  }
  .canvas {
    position: relative; width: 1200px; height: 900px;
    display: flex; align-items: center; justify-content: center; gap: 50px;
  }
  .card {
    position: relative; width: 540px; height: 310px;
    box-shadow: 0 18px 40px rgba(0,0,0,.45);
  }
  .card--front { background: var(--card-black); color: var(--text-white); font-family: "Open Sans", sans-serif; }
  .card--back  { background: var(--card-brown); display: flex; align-items: center; justify-content: center; }

  .brand {
    display: flex; align-items: center; gap: 12px;
  }
  .brand__mark {
    width: 30px; height: 30px; border-radius: 50%;
    background: var(--silver); flex: none;
  }
  .brand__name {
    font-family: "Oswald", sans-serif; font-weight: 600;
    text-transform: uppercase; letter-spacing: .5px;
    color: var(--brand-brown); white-space: nowrap;
  }
  .card--front .brand {
    position: absolute; left: 40px; top: 62px;
  }
  .card--front .brand__name { font-size: 27px; }

  .card--back .brand__mark { background: var(--silver-dark); width: 36px; height: 36px; }
  .card--back .brand__name { color: var(--brand-brown-deep); font-size: 28px; }

  .holder {
    position: absolute; left: 44px; top: 170px;
    font-size: 21px; font-weight: 700; color: var(--text-white);
    white-space: nowrap;
  }
  .divider {
    position: absolute; left: 212px; top: 140px;
    width: 1px; height: 72px; background: var(--divider);
  }
  .contact {
    position: absolute; left: 228px; top: 146px;
    list-style: none; font-size: 12.5px; color: var(--text-soft);
  }
  .contact__item { display: flex; align-items: center; gap: 8px; line-height: 22px; white-space: nowrap; }
  .contact__icon { width: 12px; height: 12px; fill: var(--text-soft); flex: none; }
  .social-dot {
    position: absolute; right: 22px; top: 150px;
    width: 36px; height: 36px; border-radius: 50%;
    background: linear-gradient(145deg, #e8e8e8, #8e8e8e);
  }
  .address {
    position: absolute; left: 0; right: 0; bottom: 42px;
    text-align: center; font-size: 15px; color: var(--text-white);
  }
</style>
</head>
<body>
<main class="canvas">
  <section class="card card--front" aria-label="Business card, front">
    <div class="brand">
      <span class="brand__mark"></span>
      <span class="brand__name">Harlow's True Grain Woodwork</span>
    </div>
    <p class="holder">Owen Harlow</p>
    <span class="divider"></span>
    <ul class="contact">
      <li class="contact__item">
        <svg class="contact__icon" viewBox="0 0 24 24" aria-hidden="true"><path d="M6.6 10.8a15.1 15.1 0 0 0 6.6 6.6l2.2-2.2c.3-.3.7-.4 1-.2 1.1.4 2.3.6 3.6.6.6 0 1 .4 1 1V20c0 .6-.4 1-1 1A17 17 0 0 1 3 4c0-.6.4-1 1-1h3.5c.6 0 1 .4 1 1 0 1.3.2 2.5.6 3.6.1.3 0 .7-.2 1l-2.3 2.2z"/></svg>
        <span>905 718-2265</span>
      </li>
      <li class="contact__item">
        <svg class="contact__icon" viewBox="0 0 24 24" aria-hidden="true"><path d="M2 5h20v14H2z M3.5 6.5 12 13l8.5-6.5" fill="none" stroke="#d9d9d9" stroke-width="2"/></svg>
        <span>harlowstruegrain@mailpost.example</span>
      </li>
    </ul>
    <span class="social-dot" aria-hidden="true"></span>
    <p class="address">412 Birchmont Rd. Niagara On-The-Lake Ont.</p>
  </section>

  <section class="card card--back" aria-label="Business card, back">
    <div class="brand">
      <span class="brand__mark"></span>
      <span class="brand__name">Harlow's True Grain Woodwork</span>
    </div>
  </section>
</main>
</body>
</html>
```